High-End Medical Center Website Design Project

This design is part of a well thought-out project by an experienced project manager / developer. The approved wireframe is attached. Creative interpretations / suggestions based on the layout encouraged.

The design is for a new state-of-the-art medical center located in Dallas, Texas. The target audience would likely be individuals (approx. 60% female /40% male) who are the healthcare decision-makers for their families. They would likely have insurance and be inclined to seek out top-quality care.

Potential clients would choose this client over others in their industry because the medical center is physician owned, meaning it is patient-focused rather than profit-focused. The facility is brand new, featuring the latest technology. (This includes an amazing waiting room featuring WiFi and docking stations.) The physicians are hand-picked by referral only.

The look of the site should be extremely clean. We are going for a well-organized, professional look with a bit of a warm glow (interpret that however you like). Use crisp corners and the colors in the logo.

Think modern, clean with some great use of color / font.

We can get lovely photography of the medical center once construction is complete. Feel free to use an "example image" behind the Featured Area ("Physician Owned. Patient-Focused") if you like. We are open to ideas.

ONE CHANGE REQUESTED IN THE WIREFRAME:

Remove the "Connect" 1/4 page footer area and replace with a quick contact form. You may swap the "Locations" area with the form if desired. Put social media icons at the top left of the page in the top header area.

(Note: Please use social media icons that match the design rather than standard icons. We preferred not placing the icons at the top, but the client requested this. Let's not bring more attention to them than necessary.)
Updates

We're custom programming this site, so there's no need to base it on a template. Also, we would prefer not to use typical "seen everywhere" stock images.Thanks.

Industry/Entity Type

Construction

Requirements
Must have
• Follow the wireframe. This has been approved.
Nice to have
• Examples of what hover states, links or dropdowns might look like.

```html
<!DOCTYPE html>
<html lang="en">
<head>
<meta charset="utf-8">
<title>Nova Medical Center</title>
<link rel="stylesheet" href="https://fonts.googleapis.com/css2?family=Roboto+Condensed:wght@400;700&family=Open+Sans:ital,wght@0,400;0,600;1,400;1,600&display=swap">
<style>
:root{
  --blue:#0d5db3;
  --blue-dark:#0a4f9c;
  --blue-band-top:#0b6ccc;
  --blue-band-bottom:#4b87bf;
  --teal:#1f8fa8;
  --teal-light:#4fb6c8;
  --ink:#333;
  --muted:#9a9a9a;
  --rule:#d9d9d9;
  --footer:#ececec;
  --footer-bar:#dedede;
  --white:#fff;
}
*{box-sizing:border-box;margin:0;padding:0}
html,body{width:1145px;height:1200px;overflow:hidden}
body{position:relative;background:var(--white);font-family:"Open Sans",Arial,sans-serif;color:var(--ink)}
.abs{position:absolute}
.cond{font-family:"Roboto Condensed","Arial Narrow",sans-serif}

/* top bar */
.social{left:120px;top:5px;display:flex;gap:6px}
.social span{width:25px;height:25px;background:var(--blue);display:block}
.call{right:118px;top:7px;font-size:19px;color:var(--blue)}
.call b{font-weight:700}
.call em{font-style:normal;color:var(--teal)}

.band{left:0;top:34px;width:1145px;height:229px;background:linear-gradient(var(--blue-band-top),var(--blue-band-bottom))}

/* hero */
.hero{left:120px;top:78px;width:897px;height:370px;background:var(--white);border-radius:4px;box-shadow:0 10px 14px -8px rgba(0,0,0,.35)}
.hero-photo{left:132px;top:132px;width:881px;height:310px;background:linear-gradient(100deg,#c9d4df 0%,#e8ecef 35%,#f0e2d6 55%,#e9c9a9 70%,#b8cde0 100%);border-bottom:5px solid var(--blue)}
.hero-title{left:300px;top:236px;width:405px;text-align:center;font-size:47px;line-height:53px;font-weight:700;color:var(--blue);text-shadow:0 0 3px #fff,0 0 6px #fff}
.hero-title .line2{color:#1a6f86}
.slide-arrow{top:342px;width:36px;height:38px;background:var(--blue);border-radius:3px;display:flex;align-items:center;justify-content:center}
.slide-arrow.prev{left:123px}
.slide-arrow.next{left:986px}
.hero-badge{top:394px;width:92px;height:48px;background:var(--blue);border-radius:46px 46px 0 0;display:flex;align-items:center;justify-content:center;padding-top:6px}

/* logo + nav */
.logo{left:120px;top:63px;width:290px;height:86px;background:var(--white);box-shadow:0 3px 5px rgba(0,0,0,.3);display:flex;align-items:center;gap:10px;padding-left:14px}
.logo i{width:20px;height:20px;background:var(--teal);display:block;flex:none}
.logo strong{font-family:"Roboto Condensed",sans-serif;font-weight:700;font-size:23px;color:var(--blue);white-space:nowrap}
.nav{left:410px;top:80px;height:55px;display:flex}
.nav a{height:55px;line-height:55px;padding:0 15px;font-size:18px;color:#444;text-decoration:none;background:linear-gradient(#f4f4f4,#dcdcdc);border-left:1px solid #c8c8c8;white-space:nowrap}
.nav a.current{color:var(--blue);background:linear-gradient(#fafafa,#e6e6e6);border-left:none}
.nav a:hover{color:var(--blue)}

/* features */
.sets{left:122px;top:528px;width:100px;text-align:center;font-size:23px;line-height:26px;color:var(--blue);font-weight:700}
.chevron{left:220px;top:470px}
.feature{top:476px;width:216px}
.feature h3{font-family:"Roboto Condensed",sans-serif;font-weight:400;font-size:23px;color:#444;padding-bottom:8px;border-bottom:1px solid var(--rule)}
.feature p{margin-top:12px;font-size:12px;line-height:20px;color:var(--muted)}
.vrule{top:540px;width:1px;height:80px;background:#eee}

/* intro */
.intro-photo{left:132px;top:670px;width:192px;height:190px;border:5px solid var(--white);box-shadow:0 0 4px rgba(0,0,0,.3);background:linear-gradient(135deg,#9fc3df,#5b9bd0 55%,#1d6fb3)}
.intro{left:341px;top:664px;width:406px}
.intro h2{font-family:"Roboto Condensed",sans-serif;font-weight:400;font-size:23px;color:var(--blue)}
.intro p{margin-top:12px;font-size:12px;line-height:19px;color:var(--muted);text-align:justify}
.intro a{display:block;margin-top:12px;font-size:10px;font-weight:600;font-style:italic;color:var(--blue);text-decoration:none}

.testi{left:779px;top:664px;width:240px;text-align:center}
.testi h2{font-family:"Roboto Condensed",sans-serif;font-weight:400;font-size:23px;color:var(--blue)}
.testi-box{position:relative;margin-top:14px;height:110px}
.testi-box svg{position:absolute;left:0;top:0}
.testi-box .body{position:relative;padding:10px 16px}
.testi-box h4{font-size:11px;font-weight:600;font-style:italic;color:var(--blue)}
.testi-box p{margin-top:6px;font-size:10px;line-height:17px;font-style:italic;color:var(--muted)}
.testi-nav{margin:20px auto 0;display:flex;gap:16px;justify-content:center}
.testi-nav span{width:28px;height:28px;border-radius:50%;background:var(--white);box-shadow:0 2px 3px rgba(0,0,0,.35);display:flex;align-items:center;justify-content:center}

/* footer */
.footer{left:0;top:895px;width:1145px;height:258px;background:var(--footer)}
.fsep{top:895px;width:2px;height:258px;background:var(--white)}
.fcol{top:923px;width:160px}
.ftitle{width:143px;height:30px;background:var(--white);display:flex;align-items:center;gap:8px;padding-left:8px;font-family:"Roboto Condensed",sans-serif;font-size:15px;color:var(--blue);white-space:nowrap;box-shadow:0 6px 6px -6px rgba(0,0,0,.3)}
.ftitle.wide{width:143px;font-size:14px;gap:5px;padding-left:6px}
.post{margin-top:20px}
.post h5{font-size:13px;font-weight:600;color:#222}
.post small{display:block;font-size:10px;color:#777;margin-top:2px}
.post time{display:block;font-size:11px;font-weight:600;font-style:italic;color:var(--blue);margin-top:2px}
.post + .post{margin-top:26px}
.fline{width:143px;height:1px;background:#7a8ea3;margin-top:6px;position:relative}
.link-btn{position:absolute;right:0;bottom:0;width:23px;height:21px;background:var(--blue);display:flex;align-items:center;justify-content:center}
.field{width:137px;height:24px;margin-top:10px;border:1px solid #c9c9c9;background:#f4f4f4;font-size:10px;font-style:italic;color:#999;padding:4px 8px}
.field.msg{height:51px}
.submit{margin-top:16px;width:73px;height:24px;background:var(--blue);color:var(--white);font-size:11px;font-weight:600;font-style:italic;text-align:center;line-height:24px}
.loc p{margin-top:14px;width:145px;font-size:11px;line-height:16px;color:#444}
.loc .row{display:flex;align-items:center;gap:14px;margin-top:26px;font-size:11px;color:#333}
.wait{margin-top:18px;width:155px}
.wait .head{display:flex;align-items:center;gap:8px;font-size:14px;color:var(--blue)}
.wait .head b{width:23px;height:19px;background:var(--blue);color:var(--white);font-size:12px;text-align:center;line-height:19px;font-weight:600}
.wait p{font-size:11px;line-height:16px;color:#444;margin-top:4px}
.wait + .wait{margin-top:12px}

.bottom{left:0;top:1153px;width:1145px;height:47px;background:var(--footer-bar)}
.copy{left:120px;top:1167px;font-size:11px;color:#555}
.links{right:118px;top:1166px;font-size:12px;color:#444}
.links a{color:var(--blue);text-decoration:none}
.links span{color:#999;margin:0 6px}
</style>
</head>
<body>

<div class="abs social" aria-label="Social links"><span></span><span></span><span></span><span></span><span></span></div>
<div class="abs call cond"><b>Call Now :</b> <em>555-014-7890</em></div>

<div class="abs band"></div>

<div class="abs hero"></div>
<div class="abs hero-photo" role="img" aria-label="Photo of a physician gently examining a patient's neck"></div>
<div class="abs hero-title cond"><div>Lorem ipsum</div><div class="line2">dolor sit amet</div></div>

<div class="abs slide-arrow prev"><svg width="12" height="16" viewBox="0 0 12 16"><path d="M10 1 2 8l8 7z" fill="#fff"/></svg></div>
<div class="abs slide-arrow next"><svg width="12" height="16" viewBox="0 0 12 16"><path d="M2 1l8 7-8 7z" fill="#fff"/></svg></div>

<div class="abs hero-badge" style="left:264px"><svg width="30" height="30" viewBox="0 0 30 30" fill="none" stroke="#fff" stroke-width="3"><path d="M8 3v9a7 7 0 0 0 14 0V3"/><path d="M15 19v4a4 4 0 0 0 8 0"/><circle cx="23" cy="21" r="3"/></svg></div>
<div class="abs hero-badge" style="left:530px"><svg width="30" height="26" viewBox="0 0 30 26" fill="#fff"><path d="M2 2h18v12H9l-5 4v-4H2z"/><path d="M22 7h6v11h-2v4l-5-4H11v-2h11z"/></svg></div>
<div class="abs hero-badge" style="left:797px"><span class="cond" style="color:#fff;font-size:32px;font-weight:700">?</span></div>

<div class="abs logo"><i></i><strong>NOVA MEDICAL CENTER</strong></div>
<nav class="abs nav cond">
  <a class="current" href="#">Why Nova</a>
  <a href="#">Phycisians</a>
  <a href="#">Specialities</a>
  <a href="#">info</a>
  <a href="#">Locations</a>
  <a href="#">Contact Us</a>
</nav>

<div class="abs sets cond">What sets us a part</div>
<svg class="abs chevron" width="30" height="165" viewBox="0 0 30 165"><path d="M3 0v55l24 26-24 26v58" fill="none" stroke="var(--blue)" stroke-width="2"/></svg>

<div class="abs feature" style="left:267px"><h3>Technology</h3><p>Lorem ipsum dolor sit amet, consecte-tur adipiscing elit. Aliquam malesuada augue eget mattis ultricies. Maecenas felis sem, pretium quis venenatis quis, sodales nec</p></div>
<div class="abs vrule" style="left:508px"></div>
<div class="abs feature" style="left:534px"><h3>Quality of care</h3><p>Lorem ipsum dolor sit amet, consecte-tur adipiscing elit. Aliquam malesuada augue eget mattis ultricies. Maecenas felis sem, pretium quis venenatis quis, sodales nec</p></div>
<div class="abs vrule" style="left:775px"></div>
<div class="abs feature" style="left:801px"><h3>Patient Exprience</h3><p>Lorem ipsum dolor sit amet, consecte-tur adipiscing elit. Aliquam malesuada augue eget mattis ultricies. Maecenas felis sem, pretium quis venenatis quis, sodales nec</p></div>

<div class="abs intro-photo" role="img" aria-label="Photo of a smiling nurse in blue scrubs holding a tablet"></div>
<section class="abs intro">
  <h2>Lorem ipsum dolor sit</h2>
  <p>Lorem ipsum dolor sit amet, consectetur adipiscing elit. Aliquam male-suada augue eget mattis ultricies. Maecenas felis sem, pretium quis venenatis quis, sodales nec dolor. Sed eu facilisis metus,</p>
  <p>Non consectetur arcu. Nam in fermentum arcu, iaculis condimentum</p>
  <p>Suspendisse consequat, diam vel lobortis pulvinar, odio lacus dapibus erat adipiscing elit. Aliquam malesuada augue eget mattis ultricies.</p>
  <a href="#">Read more....</a>
</section>

<section class="abs testi">
  <h2>Our Testimonials</h2>
  <div class="testi-box">
    <svg width="240" height="125" viewBox="0 0 240 125" fill="none" stroke="var(--blue)" stroke-width="2"><path d="M20 10Q20 1 40 1h160q20 0 20 9M20 105q0 9 20 9h62l18 10 18-10h62q20 0 20-9"/><path d="M20 10q-9 0-9 10v75q0 10 9 10M220 10q9 0 9 10v75q0 10-9 10"/></svg>
    <div class="body">
      <h4>Customer Name</h4>
      <p>Lorem ipsum dolor sit amet, consectetur adipiscing elit. Integer molestie quam a lorem ipsum dolorr molestie quam a lorem ipsum dolor sit amet.....</p>
    </div>
  </div>
  <div class="testi-nav">
    <span><svg width="8" height="10" viewBox="0 0 8 10"><path d="M7 0 0 5l7 5z" fill="var(--blue)"/></svg></span>
    <span><svg width="8" height="10" viewBox="0 0 8 10"><path d="M1 0l7 5-7 5z" fill="var(--blue)"/></svg></span>
  </div>
</section>

<footer>
  <div class="abs footer"></div>
  <div class="abs fsep" style="left:284px"></div>
  <div class="abs fsep" style="left:474px"></div>
  <div class="abs fsep" style="left:657px"></div>
  <div class="abs fsep" style="left:846px"></div>

  <div class="abs fcol" style="left:120px">
    <div class="ftitle"><svg width="18" height="14" viewBox="0 0 18 14" fill="var(--blue)"><path d="M0 0h18v14H0z"/><path d="M2 2h6v5H2zM10 2h6v1H10zM10 5h6v1H10zM2 9h14v1H2zM2 11h14v1H2z" fill="#fff"/></svg>Recent News</div>
    <div class="post"><h5>Lorem ipsum lorem</h5><small>Lorem ipsum lorem ipsua</small><time>25 / 05 / 2013</time></div>
    <div class="post"><h5>Lorem ipsum lorem</h5><small>Lorem ipsum lorem ipsua</small><time>25 / 05 / 2013</time></div>
    <div class="fline"><span class="link-btn"><svg width="13" height="13" viewBox="0 0 13 13" fill="none" stroke="#fff" stroke-width="2"><path d="M5 8 8 5M6 3l1-1a2.5 2.5 0 0 1 4 4l-1 1M7 10l-1 1a2.5 2.5 0 0 1-4-4l1-1"/></svg></span></div>
  </div>

  <div class="abs fcol" style="left:306px">
    <div class="ftitle"><svg width="20" height="16" viewBox="0 0 20 16" fill="var(--blue)"><path d="M1 1h12v8H6l-4 3V9H1z"/><path d="M15 4h4v8h-2v3l-4-3H8v-1h7z"/></svg>Recent Blog</div>
    <div class="post"><h5>Lorem ipsum lorem</h5><small>Lorem ipsum lorem ipsua</small><time>25 / 05 / 2013</time></div>
    <div class="post"><h5>Lorem ipsum lorem</h5><small>Lorem ipsum lorem ipsua</small><time>25 / 05 / 2013</time></div>
    <div class="fline"><span class="link-btn"><svg width="13" height="13" viewBox="0 0 13 13" fill="none" stroke="#fff" stroke-width="2"><path d="M5 8 8 5M6 3l1-1a2.5 2.5 0 0 1 4 4l-1 1M7 10l-1 1a2.5 2.5 0 0 1-4-4l1-1"/></svg></span></div>
  </div>

  <div class="abs fcol" style="left:496px">
    <div class="ftitle"><svg width="20" height="16" viewBox="0 0 20 16" fill="var(--blue)"><path d="M1 4h18v11H1z"/><path d="M1 4l9 6 9-6" fill="none" stroke="#fff" stroke-width="1.5"/></svg>Contact Us</div>
    <div class="field" style="margin-top:20px">Name</div>
    <div class="field">Email</div>
    <div class="field msg">Message</div>
    <div class="submit">Submit</div>
  </div>

  <div class="abs fcol loc" style="left:679px">
    <div class="ftitle"><svg width="18" height="18" viewBox="0 0 18 18" fill="var(--blue)"><path d="M9 1a5 5 0 0 0-5 5c0 4 5 9 5 9s5-5 5-9a5 5 0 0 0-5-5zm0 7a2 2 0 1 1 0-4 2 2 0 0 1 0 4z"/><path d="M1 17h16v1H1z"/></svg>Location</div>
    <p>Lorem ipsum dolor sit amet, consectetur adipisc. 012345 ABCD 0000</p>
    <div class="row"><svg width="20" height="22" viewBox="0 0 20 22" fill="var(--blue)"><path d="M3 6h10v15H3z"/><path d="M5 8h6v3H5z" fill="#fff"/><path d="M12 2h7v6h-2V4h-5z"/></svg>Call : 555-014-7890</div>
    <div class="row"><svg width="22" height="18" viewBox="0 0 22 18" fill="var(--blue)"><path d="M1 3h20v14H1z"/><path d="M1 3l10 7 10-7" fill="none" stroke="#fff" stroke-width="1.5"/></svg>info@novaclinic.com</div>
  </div>

  <div class="abs fcol" style="left:868px">
    <div class="ftitle wide"><svg width="20" height="20" viewBox="0 0 20 20" fill="none" stroke="var(--blue)" stroke-width="2"><circle cx="10" cy="10" r="8"/><text x="10" y="13.5" font-size="8" text-anchor="middle" fill="var(--blue)" stroke="none" font-family="Arial,sans-serif" font-weight="700">24</text></svg>Average wait Time</div>
    <div class="wait"><div class="head"><b>30</b>Minit wait</div><p>Lorem ipsum dolor sit amet, consectetur adipiscing elit.</p></div>
    <div class="wait"><div class="head"><b>30</b>Minit wait</div><p>Lorem ipsum dolor sit amet, consectetur adipiscing elit.</p></div>
    <div class="fline" style="margin-top:12px"><span class="link-btn"><svg width="13" height="13" viewBox="0 0 13 13" fill="none" stroke="#fff" stroke-width="2"><path d="M5 8 8 5M6 3l1-1a2.5 2.5 0 0 1 4 4l-1 1M7 10l-1 1a2.5 2.5 0 0 1-4-4l1-1"/></svg></span></div>
  </div>

  <div class="abs bottom"></div>
  <div class="abs copy">Copyright© 2013 Nova medical center</div>
  <div class="abs links"><a href="#">Site map</a><span>/</span>Privacy policy</div>
</footer>

</body>
</html>
```